Brevan Law Business cards and stationary design project

We are looking for a stationary design for business cards (double sided), 8x10, 5x7, and legal and standard envelopes.

We would like the design to match the logo that we have already.
Color palate preferred is Teal, White, grey and any others that will look good for a professional law firm.

We would like this statement: "RELATIONSHIPS. RESPECT. RESULT" to be on the back of the business cards and maybe on the stationary if it looks good.

Please see link to website for more information: www.brevan-law-example.com

Target Market(s)

Potential clients that need Attorney services.

Industry/Entity Type

Law Firm

Contact Information for Business Card

We would like the front and back to be two different colors. Current business cards are teal front, grey back and are a vertical design. We are open to options with colors.

Font styles to use
Serif

Colors
33a6d7
33b8a4
b9b9b9
5c5c5c

Requirements
Must have
• Logo supplied needs to go on the card and stationary.
• Match website color palate, www.brevan-law-example.com
• Be professional and not too wordy.
• Criminal Law, Civil Litigation, Personal Injury, Restraining Orders need to be on the card.
Nice to have
• RELATIONSHIPS. RESPECT. RESULTS. on the back of the card.
Should not have
• Not be too busy/wordy or too flashy.

```html
<!DOCTYPE html>
<html lang="en">
<head>
<meta charset="utf-8">
<title>Brevan Law – Stationery Set</title>
<link rel="stylesheet" href="https://fonts.googleapis.com/css2?family=Cinzel:wght@400;500&display=swap">
<style>
  :root {
    --backdrop: #d4d4d4;
    --paper: #ffffff;
    --charcoal: #52534f;
    --teal: #1a7f8c;
    --ink: #4a4a4a;
    --tagline: #d9d9d9;
    --rule: #9fb8bc;
  }
  * { margin: 0; padding: 0; box-sizing: border-box; }
  html, body { width: 1200px; height: 900px; overflow: hidden; }
  body {
    position: relative;
    background: var(--backdrop);
    font-family: "Cinzel", "Times New Roman", serif;
    color: var(--ink);
  }
  .sheet { position: absolute; background: var(--paper); overflow: hidden; }

  /* brand lockup */
  .brand { position: absolute; text-align: center; color: var(--teal); }
  .brand__mark { display: block; margin: 0 auto 8px; width: 10px; height: 10px; background: var(--teal); }
  .brand__name { font-weight: 400; letter-spacing: 0.04em; white-space: nowrap; }

  .contact { position: absolute; font-size: 10px; line-height: 13.5px; letter-spacing: 0.05em; white-space: nowrap; }

  /* envelope back */
  .envelope-back { left: 65px; top: 143px; width: 523px; height: 262px; }
  .envelope-back svg { position: absolute; left: 0; top: 0; }

  /* envelope front */
  .envelope-front { left: 121px; top: 256px; width: 524px; height: 262px; }
  .envelope-front .brand { left: 22px; top: 62px; width: 112px; }
  .envelope-front .brand__name { font-size: 17px; }
  .envelope-front .contact { left: 164px; top: 34px; }
  .band { position: absolute; left: 0; right: 0; bottom: 0; background: var(--charcoal); }
  .envelope-front .band { height: 20px; }

  /* business card front */
  .card-front { left: 72px; top: 538px; width: 281px; height: 169px; }
  .card-front .brand { left: 0; right: 0; top: 50px; }
  .card-front .brand__name { font-size: 13px; }
  .card-front .brand__mark { width: 7px; height: 7px; margin-bottom: 6px; }
  .card-front .contact { left: 0; right: 0; top: 95px; text-align: center; font-size: 7.5px; line-height: 10.5px; }
  .card-front .contact p + p.gap { margin-top: 8px; }

  /* business card back */
  .card-back { left: 366px; top: 540px; width: 280px; height: 167px; background: var(--charcoal); }
  .tagline { position: absolute; left: 20px; top: 14px; color: var(--tagline); font-size: 21px; line-height: 17px; letter-spacing: 0.04em; }
  .card-back .web { position: absolute; right: 20px; bottom: 16px; color: var(--tagline); font-size: 7.5px; letter-spacing: 0.12em; }

  /* letterhead */
  .letterhead { left: 664px; top: 115px; width: 476px; height: 671px; }
  .letterhead .brand { left: 20px; top: 62px; width: 124px; }
  .letterhead .brand__name { font-size: 18px; }
  .letterhead .band { height: 8px; }
  .letterhead .contact--address { right: 316px; top: 602px; text-align: right; font-size: 9px; line-height: 12px; }
  .letterhead .divider { position: absolute; left: 171px; top: 600px; width: 1px; height: 46px; background: #8c8c8c; }
  .letterhead .contact--reach { left: 181px; top: 610px; font-size: 9px; line-height: 12px; }
</style>
</head>
<body>

  <section class="sheet envelope-back" aria-label="Envelope, back">
    <svg width="523" height="262" viewBox="0 0 523 262">
      <polygon points="0,0 523,0 505,62 18,62" fill="var(--charcoal)"/>
    </svg>
  </section>

  <section class="sheet envelope-front" aria-label="Envelope, front">
    <div class="brand">
      <span class="brand__mark"></span>
      <span class="brand__name">Brevan Law</span>
    </div>
    <div class="contact">
      <p>Southern California,</p>
      <p>2200 Harbor View Blvd. #410</p>
      <p>Seaside Bay, CA 90000</p>
      <p>(555) 014-2837 &nbsp;|&nbsp; anna@brevan-law-example.com</p>
    </div>
    <div class="band"></div>
  </section>

  <section class="sheet card-front" aria-label="Business card, front">
    <div class="brand">
      <span class="brand__mark"></span>
      <span class="brand__name">Brevan Law</span>
    </div>
    <div class="contact">
      <p>Southern California, 2200 Harbor View Blvd. #410</p>
      <p>Seaside Bay, CA 90000</p>
      <p class="gap">(555) 014-2837</p>
      <p>anna@brevan-law-example.com</p>
    </div>
  </section>

  <section class="sheet card-back" aria-label="Business card, back">
    <p class="tagline">Relationships<br>Respect<br>Result</p>
    <p class="web">www.brevan-law-example.com</p>
  </section>

  <section class="sheet letterhead" aria-label="Letterhead">
    <div class="brand">
      <span class="brand__mark"></span>
      <span class="brand__name">Brevan Law</span>
    </div>
    <div class="contact contact--address">
      <p>Southern California,</p>
      <p>2200 Harbor View Blvd. #410</p>
      <p>Seaside Bay, CA 90000</p>
    </div>
    <div class="divider"></div>
    <div class="contact contact--reach">
      <p>(555) 014-2837</p>
      <p>anna@brevan-law-example.com</p>
    </div>
    <div class="band"></div>
  </section>

</body>
</html>
```